Health care technology software systems

We have a solid logo. We have company colors that will need to be used as well. We just need a great business card design. We sell to health plans but want to be modern
Updates

Need extra days to review

Target Market(s)

Health technology sector selling into Health Plans

Industry/Entity Type

Health Care Technology

Contact Information for Business Card

Name, title, address, phone number, email

Requirements
Must have
• Use of Kembrata corporate colors - Uploaded w/ our logos

```html
<!DOCTYPE html>
<html lang="en">
<head>
<meta charset="utf-8">
<title>Kembrata Business Card</title>
<link href="https://fonts.googleapis.com/css2?family=Montserrat:wght@300;400;600;700&display=swap" rel="stylesheet">
<style>
  :root {
    --backdrop: #bfbfbf;
    --card: #ffffff;
    --ink: #2b2b2b;
    --ink-soft: #6d6d6d;
    --ink-muted: #a3a3a3;
    --brand-blue: #3f5ca8;
    --brand-green: #8dbf2a;
    --brand-sky: #0a8fd6;
  }
  * { box-sizing: border-box; margin: 0; padding: 0; }
  html, body { width: 1200px; height: 1000px; overflow: hidden; }
  body {
    position: relative;
    background: var(--backdrop);
    font-family: "Montserrat", sans-serif;
  }
  .card {
    position: absolute;
    top: 320px;
    width: 544px;
    height: 310px;
    background: var(--card);
    overflow: hidden;
  }
  .card--front { left: 41px; }
  .card--back { left: 608px; }

  .card__accent { position: absolute; inset: 0; }

  .wordmark {
    position: absolute;
    left: 69px;
    top: 172px;
    display: flex;
    align-items: center;
    gap: 16px;
  }
  .wordmark__dot {
    width: 38px;
    height: 38px;
    border-radius: 50%;
    background: var(--brand-blue);
  }
  .wordmark__name {
    font-weight: 300;
    font-size: 40px;
    letter-spacing: 0.5px;
    color: var(--ink);
    line-height: 1;
  }

  .contact {
    position: absolute;
    left: 281px;
    top: 106px;
    color: var(--ink-soft);
  }
  .contact__name { font-weight: 700; font-size: 17px; line-height: 22px; }
  .contact__title { font-weight: 300; font-size: 16px; line-height: 20px; color: var(--ink-muted); }
  .contact__list { list-style: none; margin-top: 18px; }
  .contact__item {
    display: flex;
    align-items: center;
    gap: 7px;
    font-weight: 600;
    font-size: 13px;
    height: 26px;
  }
  .contact__item--address { margin-top: 4px; }
  .contact__icon { width: 19px; height: 16px; flex: none; }
</style>
</head>
<body>
  <section class="card card--front" aria-label="Card front">
    <svg class="card__accent" viewBox="0 0 544 310" aria-hidden="true">
      <circle cx="500" cy="200" r="165" fill="var(--brand-blue)"/>
    </svg>
    <div class="wordmark">
      <span class="wordmark__dot"></span>
      <span class="wordmark__name">kembrata</span>
    </div>
  </section>

  <section class="card card--back" aria-label="Card back">
    <svg class="card__accent" viewBox="0 0 544 310">
      <defs>
        <linearGradient id="building-tone" x1="0" y1="0" x2="0.6" y2="1">
          <stop offset="0" stop-color="var(--brand-green)"/>
          <stop offset="0.45" stop-color="#4aa85a"/>
          <stop offset="1" stop-color="var(--brand-sky)"/>
        </linearGradient>
      </defs>
      <circle cx="60" cy="150" r="150" fill="url(#building-tone)" role="img" aria-label="Photo of a modern glass office building"/>
    </svg>
    <div class="contact">
      <p class="contact__name">Name</p>
      <p class="contact__title">title</p>
      <ul class="contact__list">
        <li class="contact__item">
          <svg class="contact__icon" viewBox="0 0 19 16" aria-hidden="true"><path d="M4 1.5l2.6 2.8-1.4 2a8.5 8.5 0 0 0 4.5 4.6l2-1.4 2.8 2.6-1.6 2.2C7.5 14 3 9.5 1.9 3.1z" fill="var(--ink-soft)"/></svg>
          877-555-0142
        </li>
        <li class="contact__item">
          <svg class="contact__icon" viewBox="0 0 19 16" aria-hidden="true"><rect x="1" y="2.5" width="17" height="11" fill="none" stroke="var(--ink-soft)" stroke-width="1.2"/><path d="M1 2.5l8.5 6.5 8.5-6.5M1 13.5l6-5M18 13.5l-6-5" fill="none" stroke="var(--ink-soft)" stroke-width="1"/></svg>
          info@kembrata.com
        </li>
        <li class="contact__item">
          <svg class="contact__icon" viewBox="0 0 19 16" aria-hidden="true"><g fill="none" stroke="var(--ink-soft)" stroke-width="1"><circle cx="9.5" cy="8" r="7"/><ellipse cx="9.5" cy="8" rx="3" ry="7"/><path d="M2.5 8h14M3.5 4.5h12M3.5 11.5h12"/></g></svg>
          kembrata.com
        </li>
        <li class="contact__item contact__item--address">
          <svg class="contact__icon" viewBox="0 0 19 16" aria-hidden="true"><path d="M9.5 15.5S4.5 9.8 4.5 6a5 5 0 0 1 10 0c0 3.8-5 9.5-5 9.5z" fill="none" stroke="var(--ink-soft)" stroke-width="1.1"/><circle cx="9.5" cy="6" r="1.8" fill="none" stroke="var(--ink-soft)" stroke-width="1.1"/></svg>
          Lakemont, Oregon
        </li>
      </ul>
    </div>
  </section>
</body>
</html>
```